NEED VIBRANT DIGTAL MENUS

NEED A NEW DESIGN FOR MENU SCREENS

SEE ATTACHED FOR EXISTING MENUS

Requirements
Must have
• FLOW. COLOR. ORGANIZATION. SOPHISTICATION.
Nice to have
• INCORPORATE LOGO IN DESIGNS

```html
<!DOCTYPE html>
<html lang="en">
<head>
<meta charset="utf-8">
<title>Harlowfield Menu Board</title>
<link href="https://fonts.googleapis.com/css2?family=Alfa+Slab+One&family=Roboto+Slab:wght@400;500;600;700&family=Poppins:wght@500;700&display=swap" rel="stylesheet">
<style>
:root{
  --brown:#7e2e07;
  --brown-deep:#6e2604;
  --rust:#a63d0c;
  --cream:#fde093;
  --cream-soft:#fee9b4;
  --title-gold:#fddc8c;
  --gold:#c8963f;
  --gold-dark:#7b3d0b;
  --white:#ffffff;
  --photo-warm:#d9a25a;
  --photo-dark:#8d4d1f;
}
*{margin:0;padding:0;box-sizing:border-box}
html,body{width:693px;height:1200px;overflow:hidden;background:var(--white)}
.menu{position:relative;width:693px;height:1200px;overflow:hidden;background:var(--white);font-family:"Poppins",sans-serif;color:var(--brown)}
.abs{position:absolute}

/* header */
.header-band{left:0;top:0;width:693px;height:126px;background:var(--brown)}
.brand-disc{left:36px;top:12px;width:142px;height:142px;border-radius:50%;background:var(--white);border:4px solid var(--brown);display:flex;align-items:center;justify-content:center;text-align:center}
.brand-name{font-family:"Roboto Slab",serif;font-weight:700;font-size:19px;line-height:1.1;color:var(--brown)}
.town-title{left:202px;top:30px;width:440px;text-align:center;font-family:"Alfa Slab One",serif;font-size:47px;letter-spacing:1px;line-height:1;white-space:nowrap;color:var(--title-gold)}
.section-pill{background:var(--brown);border-radius:30px;color:var(--white);font-family:"Alfa Slab One",serif;display:flex;align-items:center;justify-content:center;line-height:1;white-space:nowrap}
.pill-breakfast{left:209px;top:92px;width:276px;height:48px;font-size:31px;border:3px solid var(--white);box-shadow:0 0 0 2px var(--brown)}

/* breakfast */
.b-band{left:0;width:693px;height:37px;background:linear-gradient(90deg,var(--rust),var(--brown) 30%,var(--brown))}
.b-photo{width:103px;height:76px;border:2px solid var(--brown);border-bottom:none;border-radius:4px 4px 0 0;background:var(--white);padding:6px 8px 0}
.b-photo.light{border-color:var(--cream)}
.b-photo span{display:block;width:100%;height:100%;border-radius:40% 40% 20% 20%;background:radial-gradient(ellipse at 50% 40%,#f3c46f,var(--photo-warm) 60%,#b2702e)}
.b-name{width:103px;height:37px;display:flex;align-items:center;justify-content:center;text-align:center;font-family:"Roboto Slab",serif;font-weight:500;font-size:11px;line-height:1.2;color:var(--white);white-space:nowrap}
.b-name.small{font-size:7.5px;width:110px;margin-left:-3px}
.b-price{width:103px;height:26px;background:var(--cream);border-radius:0 0 4px 4px;display:flex;align-items:center;justify-content:center;font-weight:700;font-size:17px;color:var(--brown)}

/* rules */
.rule{height:3px;background:var(--cream)}
.pill-pizza{left:271px;top:476px;width:151px;height:45px;font-size:34px}
.pill-burgers{left:63px;top:892px;width:227px;height:45px;font-size:33px}
.pill-subs{left:445px;top:892px;width:133px;height:45px;font-size:33px}

/* pizza */
.p-band{left:0;width:693px;height:19px;background:linear-gradient(90deg,#d7a85a,var(--brown) 6%,var(--brown) 33%,#d7a85a 34.5%,var(--brown) 37%,var(--brown) 66%,#d7a85a 67.5%,var(--brown) 70%)}
.p-band.four{background:linear-gradient(90deg,#d7a85a,var(--brown) 5%,var(--brown) 27%,#d7a85a 28.5%,var(--brown) 31%,var(--brown) 49%,#d7a85a 50.5%,var(--brown) 53%,var(--brown) 72%,#d7a85a 73.5%,var(--brown) 76%)}
.p-title{font-family:"Roboto Slab",serif;font-weight:500;font-size:13px;line-height:19px;color:var(--white);white-space:nowrap}
.p-photo{border-radius:50% 0 0 50%;background:radial-gradient(circle at 60% 45%,#e8a95a,#c2682e 55%,#5a2a10 90%)}
.p-info{background:var(--cream);padding:4px 4px 0}
.p-prices{display:flex}
.p-size{flex:1;padding-left:5px;white-space:nowrap}
.p-size+.p-size{border-left:1px solid var(--brown)}
.p-label{font-family:"Roboto Slab",serif;font-weight:500;font-size:8px;line-height:1.1;white-space:nowrap}
.p-amt{font-weight:700;font-size:12.5px;line-height:1.3;white-space:nowrap}
.p-amt sup{font-size:7px}
.p-tops{background:var(--white);margin-top:5px;padding:2px 4px;height:27px}
.p-tops b{display:block;font-size:8px;line-height:1.1}
.p-tops small{display:block;font-size:5.2px;line-height:1.3;font-weight:500;text-transform:uppercase;white-space:nowrap}
.p-card4{background:var(--cream);height:77px;padding:4px 4px}
.p-card4 .p-size{padding-left:4px}
.p-card4 .p-size:first-child{padding-left:0}
.p-card4 .p-tops{position:absolute;left:4px;bottom:3px;width:60%;margin:0}
.p-photo4{border-radius:50% 0 0 50%;background:radial-gradient(circle at 55% 45%,#e07a4a,#bb4f2a 55%,#6e2b10 90%)}

/* burgers */
.g-photo{width:51px;height:47px;border-radius:45% 45% 30% 30%;background:linear-gradient(180deg,#d89a4d,#8a4f1f 55%,#c88a3e)}
.g-label{width:101px;height:47px;background:var(--cream)}
.g-name{height:22px;background:var(--brown);color:var(--white);font-family:"Roboto Slab",serif;font-weight:500;font-size:8.5px;line-height:1.2;display:flex;align-items:center;justify-content:center;text-align:center;white-space:nowrap}
.g-price{height:25px;display:flex;align-items:center;justify-content:center;font-weight:700;font-size:16px}

/* subs */
.s-photo{width:59px;height:38px;border-radius:40%;background:linear-gradient(180deg,#d9a060,#c5705a 50%,#b9844a)}
.s-block{width:111px;height:42px;background:linear-gradient(90deg,#a66a2b,var(--gold-dark) 25%,var(--gold-dark) 75%,#a66a2b)}
.s-name{height:13px;background:linear-gradient(90deg,#d9b46c,var(--cream-soft) 50%,#d9b46c);font-family:"Roboto Slab",serif;font-weight:500;font-size:9px;line-height:13px;text-align:center;color:var(--brown);white-space:nowrap}
.s-prices{display:flex;justify-content:center;padding-top:2px}
.s-size{text-align:center;padding:0 4px;color:var(--white);white-space:nowrap}
.s-size+.s-size{border-left:1px solid var(--cream)}
.s-size em{display:block;font-style:normal;font-size:6px;line-height:1.2}
.s-size strong{display:block;font-size:12.5px;line-height:1.2;color:var(--cream-soft)}
.s-size strong sup{font-size:7px}
.footer-band{left:0;top:1180px;width:693px;height:20px;background:var(--brown)}
</style>
</head>
<body>
<main class="menu">
  <header>
    <div class="abs header-band"></div>
    <div class="abs brand-disc"><span class="brand-name">Meadowline<br>Market</span></div>
    <h1 class="abs town-title">HARLOWFIELD</h1>
    <h2 class="abs section-pill pill-breakfast">BREAKFAST</h2>
  </header>

  <section class="breakfast">
    <div class="abs b-band" style="top:233px"></div>
    <div class="abs b-band" style="top:387px"></div>

    <div class="abs b-photo" style="left:54px;top:158px"><span role="img" aria-label="Bacon, egg and cheese biscuit"></span></div>
    <div class="abs b-photo" style="left:173px;top:158px"><span role="img" aria-label="Sausage, egg and cheese biscuit"></span></div>
    <div class="abs b-photo" style="left:293px;top:158px"><span role="img" aria-label="Ham, egg and cheese biscuit"></span></div>
    <div class="abs b-photo" style="left:412px;top:158px"><span role="img" aria-label="Steak, egg and cheese biscuit"></span></div>
    <div class="abs b-photo" style="left:532px;top:158px"><span role="img" aria-label="Chicken, egg and cheese biscuit"></span></div>

    <div class="abs b-name" style="left:54px;top:233px">BACON, EGG,<br>&amp; CHEESE</div>
    <div class="abs b-name" style="left:173px;top:233px">SAUSAGE, EGG,<br>&amp; CHEESE</div>
    <div class="abs b-name" style="left:293px;top:233px">HAM, EGG,<br>&amp; CHEESE</div>
    <div class="abs b-name" style="left:412px;top:233px">STEAK, EGG,<br>&amp; CHEESE</div>
    <div class="abs b-name" style="left:532px;top:233px">CHICKEN, EGG,<br>&amp; CHEESE</div>

    <div class="abs b-price" style="left:54px;top:270px">$4.29</div>
    <div class="abs b-price" style="left:173px;top:270px">$4.29</div>
    <div class="abs b-price" style="left:293px;top:270px">$5.49</div>
    <div class="abs b-price" style="left:412px;top:270px">$7.49</div>
    <div class="abs b-price" style="left:532px;top:270px">$6.99</div>

    <div class="abs b-photo light" style="left:54px;top:312px"><span role="img" aria-label="Bologna, egg and cheese biscuit"></span></div>
    <div class="abs b-photo light" style="left:173px;top:312px"><span role="img" aria-label="Classic BLT on a biscuit"></span></div>
    <div class="abs b-photo light" style="left:293px;top:312px"><span role="img" aria-label="Two croissant breakfast sandwiches"></span></div>
    <div class="abs b-photo light" style="left:412px;top:312px"><span role="img" aria-label="Bacon, sausage, egg and cheese biscuit"></span></div>
    <div class="abs b-photo light" style="left:532px;top:312px"><span role="img" aria-label="Breakfast platter with eggs, hash brown, ham and biscuit"></span></div>

    <div class="abs b-name" style="left:54px;top:387px">BOLOGNA, EGG,<br>&amp; CHEESE</div>
    <div class="abs b-name" style="left:173px;top:387px">CLASSIC BLT</div>
    <div class="abs b-name small" style="left:293px;top:387px">SAUSAGE, EGG, &amp; CHEESE<br>OR BACON, EGG, &amp; CHEESE</div>
    <div class="abs b-name" style="left:407px;top:387px;width:114px">BACON, SAUSAGE,<br>EGG &amp; CHEESE</div>
    <div class="abs b-name" style="left:532px;top:387px">BREAKFAST<br>PLATTER</div>

    <div class="abs b-price" style="left:54px;top:424px">$4.29</div>
    <div class="abs b-price" style="left:173px;top:424px">$4.29</div>
    <div class="abs b-price" style="left:293px;top:424px">$5.49</div>
    <div class="abs b-price" style="left:412px;top:424px">$7.49</div>
    <div class="abs b-price" style="left:532px;top:424px">$6.99</div>
  </section>

  <section class="pizza">
    <div class="abs rule" style="left:0;top:497px;width:693px"></div>
    <h2 class="abs section-pill pill-pizza">PIZZA</h2>

    <div class="abs p-band" style="top:537px"></div>
    <span class="abs p-title" style="right:485px;top:537px">SUPREME</span>
    <span class="abs p-title" style="right:261px;top:537px">PHILLY STEAK PIZZA</span>
    <span class="abs p-title" style="right:42px;top:537px">BACON CHEESEBURGER</span>

    <div class="abs p-photo" role="img" aria-label="Supreme pizza" style="left:23px;top:560px;width:62px;height:68px"></div>
    <div class="abs p-info" style="left:84px;top:556px;width:131px;height:77px">
      <div class="p-prices"><div class="p-size"><div class="p-label">LARGE</div><div class="p-amt">$15.<sup>99</sup></div></div><div class="p-size"><div class="p-label">EXTRA LARGE</div><div class="p-amt">$17.<sup>99</sup></div></div></div>
      <div class="p-tops"><b>TOPPINGS:</b><small>Pepperoni, sausage, onions,<br>green peppers and mushrooms</small></div>
    </div>

    <div class="abs p-photo" role="img" aria-label="Philly steak pizza" style="left:243px;top:560px;width:62px;height:68px"></div>
    <div class="abs p-info" style="left:305px;top:556px;width:131px;height:77px">
      <div class="p-prices"><div class="p-size"><div class="p-label">LARGE</div><div class="p-amt">$16.<sup>99</sup></div></div><div class="p-size"><div class="p-label">EXTRA LARGE</div><div class="p-amt">$18.<sup>99</sup></div></div></div>
      <div class="p-tops"><b>TOPPINGS:</b><small>Philly steak, onions,<br>green peppers and mushrooms</small></div>
    </div>

    <div class="abs p-photo" role="img" aria-label="Bacon cheeseburger pizza" style="left:464px;top:560px;width:62px;height:68px"></div>
    <div class="abs p-info" style="left:526px;top:556px;width:131px;height:77px">
      <div class="p-prices"><div class="p-size"><div class="p-label">LARGE</div><div class="p-amt">$16.<sup>99</sup></div></div><div class="p-size"><div class="p-label">EXTRA LARGE</div><div class="p-amt">$18.<sup>99</sup></div></div></div>
      <div class="p-tops"><b>TOPPINGS:</b><small>Ground beef and bacon<br>with cheddar</small></div>
    </div>

    <div class="abs p-band" style="top:655px"></div>
    <span class="abs p-title" style="right:490px;top:655px">VEGGIE LOVERS</span>
    <span class="abs p-title" style="right:269px;top:655px">MEAT LOVERS SUPREME</span>
    <span class="abs p-title" style="right:49px;top:655px">CHEESE</span>

    <div class="abs p-photo" role="img" aria-label="Veggie lovers pizza" style="left:23px;top:678px;width:62px;height:68px"></div>
    <div class="abs p-info" style="left:84px;top:674px;width:130px;height:77px">
      <div class="p-prices"><div class="p-size"><div class="p-label">LARGE</div><div class="p-amt">$13.<sup>99</sup></div></div><div class="p-size"><div class="p-label">EXTRA LARGE</div><div class="p-amt">$15.<sup>99</sup></div></div></div>
      <div class="p-tops"><b>TOPPINGS:</b><small>Pepperoni, sausage, onions,<br>green peppers and mushrooms</small></div>
    </div>

    <div class="abs p-photo" role="img" aria-label="Meat lovers supreme pizza" style="left:243px;top:678px;width:62px;height:68px"></div>
    <div class="abs p-info" style="left:305px;top:674px;width:131px;height:77px">
      <div class="p-prices"><div class="p-size"><div class="p-label">LARGE</div><div class="p-amt">$16.<sup>99</sup></div></div><div class="p-size"><div class="p-label">EXTRA LARGE</div><div class="p-amt">$18.<sup>99</sup></div></div></div>
      <div class="p-tops"><b>TOPPINGS:</b><small>Pepperoni, sausage, bacon, ham,<br>onions, green peppers&amp; mushrooms</small></div>
    </div>

    <div class="abs p-photo" role="img" aria-label="Cheese pizza" style="left:464px;top:678px;width:62px;height:68px;background:radial-gradient(circle at 60% 45%,#f7d27a,#eaa64a 60%,#5a2a10 92%)"></div>
    <div class="abs p-info" style="left:526px;top:674px;width:131px;height:77px">
      <div class="p-prices"><div class="p-size"><div class="p-label">LARGE</div><div class="p-amt">$11.<sup>99</sup></div></div><div class="p-size"><div class="p-label">EXTRA LARGE</div><div class="p-amt">$12.<sup>99</sup></div></div></div>
      <div class="p-tops"><b>TOPPINGS:</b><small>Ground beef and bacon<br>with cheddar</small></div>
    </div>

    <div class="abs p-band four" style="top:774px"></div>
    <span class="abs p-title" style="left:50px;top:774px">MEAT LOVERS</span>
    <span class="abs p-title" style="left:232px;top:774px">HAWAIIAN</span>
    <span class="abs p-title" style="left:378px;top:774px">ONE TOPPING</span>
    <span class="abs p-title" style="left:526px;top:774px">CREATE YOUR OWN</span>

    <div class="abs p-card4" style="left:39px;top:793px;width:133px">
      <div class="p-prices"><div class="p-size"><div class="p-label">LARGE</div><div class="p-amt">$15.<sup>99</sup></div></div><div class="p-size"><div class="p-label">EXTRA LARGE</div><div class="p-amt">$17.<sup>99</sup></div></div></div>
      <div class="abs p-photo4" role="img" aria-label="Meat lovers pizza" style="right:0;top:34px;width:50px;height:42px"></div>
      <div class="p-tops" style="width:78px"><b>TOPPINGS:</b><small>Pepperoni, sausage,<br>bacon, ham</small></div>
    </div>

    <div class="abs p-card4" style="left:206px;top:793px;width:123px">
      <div class="p-prices"><div class="p-size"><div class="p-label">LARGE</div><div class="p-amt">$14.<sup>99</sup></div></div><div class="p-size"><div class="p-label">EXTRA LARGE</div><div class="p-amt">$16.<sup>99</sup></div></div></div>
      <div class="abs p-photo4" role="img" aria-label="Hawaiian pizza" style="right:0;top:34px;width:46px;height:42px;background:radial-gradient(circle at 55% 45%,#f0c070,#d29048 60%,#6e2b10 92%)"></div>
      <div class="p-tops" style="width:72px"><b>TOPPINGS:</b><small>Pepperoni, sausage,<br>bacon, ham</small></div>
    </div>

    <div class="abs p-card4" style="left:362px;top:793px;width:129px">
      <div class="p-prices"><div class="p-size"><div class="p-label">LARGE</div><div class="p-amt">$12.<sup>99</sup></div></div><div class="p-size"><div class="p-label">EXTRA LARGE</div><div class="p-amt">$14.<sup>99</sup></div></div></div>
      <div class="abs p-photo4" role="img" aria-label="One topping pepperoni pizza" style="right:0;top:34px;width:50px;height:42px"></div>
      <div class="abs" style="left:5px;bottom:3px;width:72px;height:32px;background:var(--white)"></div>
    </div>

    <div class="abs p-card4" style="left:523px;top:793px;width:137px">
      <div class="p-prices"><div class="p-size"><div class="p-label">LARGE</div><div class="p-amt">$15.<sup>99</sup></div></div><div class="p-size"><div class="p-label">EXTRA LARGE</div><div class="p-amt">$17.<sup>99</sup></div></div></div>
      <div class="abs p-photo4" role="img" aria-label="Build your own pizza with mixed slices" style="right:2px;top:34px;width:44px;height:42px;border-radius:50%;background:radial-gradient(circle,#f1b77a,#d77a4e 60%,#b24a2a)"></div>
      <div class="p-tops" style="width:80px"><b>TOPPINGS:</b><small>Pepperoni, sausage,<br>bacon, ham</small></div>
    </div>
  </section>

  <section class="burgers">
    <div class="abs rule" style="left:0;top:912px;width:693px"></div>
    <h2 class="abs section-pill pill-burgers">BURGERS</h2>

    <div class="abs g-photo" role="img" aria-label="Cheeseburger" style="left:23px;top:957px"></div>
    <div class="abs g-label" style="left:74px;top:957px"><div class="g-name">1/3 LB<br>CHEESEBURGER</div><div class="g-price">$5.49</div></div>
    <div class="abs g-label" style="left:176px;top:957px"><div class="g-name">2/3 LB<br>CHEESEBURGER</div><div class="g-price">$8.49</div></div>
    <div class="abs g-photo" role="img" aria-label="Large cheeseburger" style="left:277px;top:955px"></div>

    <div class="abs g-photo" role="img" aria-label="Bacon cheeseburger" style="left:23px;top:1025px"></div>
    <div class="abs g-label" style="left:74px;top:1025px"><div class="g-name">BACON<br>CHEESEBURGER</div><div class="g-price">$7.49</div></div>
    <div class="abs g-label" style="left:176px;top:1025px"><div class="g-name">SWISS MUSHROOM<br>BURGER</div><div class="g-price">$7.49</div></div>
    <div class="abs g-photo" role="img" aria-label="Swiss mushroom burger" style="left:277px;top:1025px"></div>

    <div class="abs g-photo" role="img" aria-label="Double bacon cheeseburger" style="left:23px;top:1087px"></div>
    <div class="abs g-label" style="left:74px;top:1087px"><div class="g-name">DOUBLE BACON<br>CHEESEBURGER</div><div class="g-price">$9.99</div></div>
    <div class="abs g-label" style="left:176px;top:1087px"><div class="g-name">BOLOGNA BURGUR<br>WITH CHEESE</div><div class="g-price">$5.99</div></div>
    <div class="abs g-photo" role="img" aria-label="Bologna burger with cheese" style="left:277px;top:1087px"></div>
  </section>

  <section class="subs">
    <h2 class="abs section-pill pill-subs">SUBS</h2>

    <div class="abs s-photo" role="img" aria-label="Ham and cheese sub" style="left:345px;top:959px"></div>
    <div class="abs s-block" style="left:404px;top:957px"><div class="s-name">HAM &amp; CHEESE</div><div class="s-prices"><div class="s-size"><em>6 INCH</em><strong>$7.<sup>99</sup></strong></div><div class="s-size"><em>12 INCH</em><strong>$11.<sup>99</sup></strong></div></div></div>
    <div class="abs s-block" style="left:515px;top:957px"><div class="s-name">TURKEY &amp; CHEESE</div><div class="s-prices"><div class="s-size"><em>6 INCH</em><strong>$7.<sup>99</sup></strong></div><div class="s-size"><em>12 INCH</em><strong>$11.<sup>99</sup></strong></div></div></div>
    <div class="abs s-photo" role="img" aria-label="Turkey and cheese sub" style="left:626px;top:959px"></div>

    <div class="abs s-photo" role="img" aria-label="Chipotle chicken sub" style="left:345px;top:1013px"></div>
    <div class="abs s-block" style="left:404px;top:1012px"><div class="s-name">CHIPOTLE CHICKEN</div><div class="s-prices"><div class="s-size"><em>6 INCH</em><strong>$8.<sup>99</sup></strong></div><div class="s-size"><em>12 INCH</em><strong>$12.<sup>99</sup></strong></div></div></div>
    <div class="abs s-block" style="left:515px;top:1012px"><div class="s-name">ITALIAN</div><div class="s-prices"><div class="s-size"><em>6 INCH</em><strong>$8.<sup>99</sup></strong></div><div class="s-size"><em>12 INCH</em><strong>$12.<sup>99</sup></strong></div></div></div>
    <div class="abs s-photo" role="img" aria-label="Italian sub" style="left:626px;top:1013px"></div>

    <div class="abs s-photo" role="img" aria-label="Club sub" style="left:345px;top:1067px"></div>
    <div class="abs s-block" style="left:404px;top:1066px"><div class="s-name">CLUB</div><div class="s-prices"><div class="s-size"><em>6 INCH</em><strong>$8.<sup>99</sup></strong></div><div class="s-size"><em>12 INCH</em><strong>$12.<sup>99</sup></strong></div></div></div>
    <div class="abs s-block" style="left:515px;top:1066px"><div class="s-name">GRILLED CHICKEN</div><div class="s-prices"><div class="s-size"><em>6 INCH</em><strong>$7.<sup>99</sup></strong></div><div class="s-size"><em>12 INCH</em><strong>$11.<sup>99</sup></strong></div></div></div>
    <div class="abs s-photo" role="img" aria-label="Grilled chicken sub" style="left:626px;top:1067px"></div>

    <div class="abs s-photo" role="img" aria-label="Steak and cheese sub" style="left:414px;top:1122px;width:46px"></div>
    <div class="abs s-block" style="left:460px;top:1120px;width:105px"><div class="s-name">STEAK &amp; CHEESE</div><div class="s-prices"><div class="s-size"><em>6 INCH</em><strong>$8.99</strong></div><div class="s-size"><em>12 INCH</em><strong>$12.99</strong></div></div></div>
    <div class="abs s-photo" role="img" aria-label="Steak and cheese sub" style="left:565px;top:1122px;width:50px"></div>
  </section>

  <div class="abs footer-band"></div>
</main>
</body>
</html>
```